Broschüre für Hausmeisterservice
Zielgruppe
Unser Hausmeisterservice bietet zuverlässige und professionelle Dienstleistungen rund um die Immobilie. Dazu gehören unter anderem die Pflege und Wartung von Gebäuden, kleinere Reparaturen, Reinigungsarbeiten, Gartenpflege sowie Winterdienst. Unser Ziel ist es, Eigentümern, Hausverwaltungen und Unternehmen einen sorgenfreien Rundum-Service zu bieten, damit ihre Immobilien stets gepflegt und funktionstüchtig sind. Unsere Zielgruppe sind somit Hausverwaltungen, Eigentümergemeinschaften, Firmen und Privatpersonen, die Wert auf eine gepflegte Immobilie legen und einen zuverlässigen Partner suchen.
Aufgabenstellung
Corporate Design und Kommunikation:
Freundlich, vertrauenswürdig und professionell wirken
Klare, verständliche Sprache verwenden
Visuelle Elemente, die Sauberkeit, Ordnung und gepflegte Immobilien ausstrahlen
Call-to-Action:
Klare Aufforderungen zur Kontaktaufnahme, Angebotserstellung oder Terminvereinbarung.

```html
<!DOCTYPE html>
<html lang="de">
<head>
<meta charset="utf-8">
<title>Hausdienst Velmar – Broschüre</title>
<link rel="stylesheet" href="https://fonts.googleapis.com/css2?family=Poppins:ital,wght@0,400;0,600;0,700;1,400;1,700&display=swap">
<style>
  :root {
    --backdrop: #b8b8bd;
    --paper: #f6f6f6;
    --coral: #ec6f5f;
    --coral-soft: #f1877a;
    --ink: #1d1d22;
    --ink-soft: #3a3a40;
    --white: #ffffff;
  }
  * { box-sizing: border-box; margin: 0; padding: 0; }
  html, body { width: 720px; height: 1200px; overflow: hidden; }
  body {
    background: var(--backdrop);
    font-family: "Poppins", sans-serif;
    color: var(--ink);
    position: relative;
  }
  .panel {
    position: absolute;
    top: 260px;
    width: 320px;
    height: 680px;
    background: linear-gradient(180deg, var(--white) 0%, var(--paper) 100%);
    box-shadow: 0 8px 22px rgba(0,0,0,0.18);
    overflow: hidden;
  }
  .panel--back { left: 30px; }
  .panel--front { left: 370px; }

  /* Front cover */
  .brand-tab {
    position: absolute;
    left: 82px; top: -2px;
    width: 156px; height: 178px;
    background: var(--white);
    border: 2px solid var(--coral-soft);
    border-top: none;
    border-radius: 0 0 78px 78px;
    box-shadow: 0 8px 14px rgba(0,0,0,0.12);
    display: flex; flex-direction: column; align-items: center; justify-content: center;
    gap: 8px;
    padding-top: 10px;
  }
  .brand-dot {
    width: 44px; height: 44px; border-radius: 50%;
    background: var(--coral);
  }
  .brand-name {
    font-weight: 700; font-size: 10.5px; letter-spacing: 0.2px;
    color: var(--ink); text-transform: uppercase;
  }
  .brand-claim {
    font-size: 5px; color: var(--ink-soft); text-transform: uppercase;
    letter-spacing: 0.3px; margin-top: -6px;
  }
  .headline {
    position: absolute; top: 238px; left: 0; right: 0;
    text-align: center; font-size: 15px; line-height: 1.3;
    font-weight: 400; color: var(--ink);
  }
  .headline em { font-weight: 700; }
  .subline {
    position: absolute; top: 310px; left: 0; right: 0;
    text-align: center; font-size: 7.5px; line-height: 1.4;
    font-style: italic; color: var(--ink-soft);
  }
  .cta {
    position: absolute; top: 386px; left: 61px;
    width: 200px; height: 38px; border-radius: 6px;
    background: var(--coral);
    color: var(--white); font-size: 10px; font-style: italic;
    display: flex; align-items: center; justify-content: center;
    box-shadow: 0 8px 12px rgba(236,111,95,0.28);
  }
  .house-photo {
    position: absolute; left: 0; right: 0; bottom: 0; height: 230px;
    background: linear-gradient(160deg, rgba(255,255,255,0) 0%, rgba(232,230,228,0.9) 22%, #a98563 45%, #3a3c42 70%, #2a2b30 100%);
    clip-path: polygon(0 40%, 100% 0, 100% 100%, 0 100%);
  }

  /* Back panel */
  .contact {
    position: absolute; left: 0; right: 0;
    display: flex; flex-direction: column; align-items: center; gap: 12px;
  }
  .contact--phone { top: 58px; }
  .contact--mail { top: 150px; }
  .contact-icon { width: 52px; height: 46px; filter: drop-shadow(0 4px 5px rgba(0,0,0,0.18)); }
  .contact-text { font-size: 12.5px; color: var(--ink); letter-spacing: 0.2px; }
  .worker-illustration {
    position: absolute; left: 0; right: 0; bottom: 0; height: 400px;
    background: radial-gradient(ellipse at 50% 60%, #f2a34a 0%, #e8683f 30%, #3aa6a0 55%, rgba(246,246,246,0) 78%);
  }
</style>
</head>
<body>
  <section class="panel panel--back" aria-label="Rückseite mit Kontakt">
    <div class="contact contact--phone">
      <svg class="contact-icon" viewBox="0 0 52 46" aria-hidden="true">
        <path d="M26 2 C38 2 50 8 50 22 C50 36 40 44 26 44 C12 44 2 36 2 22 C2 8 14 2 26 2 Z" fill="#ec6f5f"/>
        <path d="M20 14 l4 0 l2 6 l-3 2 c1 3 3 5 6 6 l2 -3 l6 2 l0 4 c-10 1 -18 -7 -17 -17 z" fill="#fff"/>
      </svg>
      <p class="contact-text">+4930555018427</p>
    </div>
    <div class="contact contact--mail">
      <svg class="contact-icon" viewBox="0 0 52 46" aria-hidden="true">
        <path d="M26 2 C38 2 50 8 50 22 C50 36 40 44 26 44 C12 44 2 36 2 22 C2 8 14 2 26 2 Z" fill="#ec6f5f"/>
        <rect x="15" y="15" width="22" height="15" rx="1.5" fill="#fff"/>
        <path d="M15 16 L26 24 L37 16" stroke="#ec6f5f" stroke-width="2" fill="none"/>
      </svg>
      <p class="contact-text">info@hausdienst-velmar.example</p>
    </div>
    <div class="worker-illustration" role="img" aria-label="Illustration eines Hausmeisters mit Werkzeugkiste, Farbroller und Besen"></div>
  </section>

  <section class="panel panel--front" aria-label="Titelseite">
    <div class="brand-tab">
      <span class="brand-dot" aria-hidden="true"></span>
      <span class="brand-name">Hausdienst Velmar</span>
      <span class="brand-claim">Gepflegt, pünktlich, verlässlich</span>
    </div>
    <h1 class="headline">Ihr <em>zuverlässiger</em><br><em>Partner</em> für <em>alle Reinigungs</em><br><em>-und Wartungsdienstleistungen</em></h1>
    <p class="subline">Professionelle Reinigung, Gartenpflege,<br>Reparaturarbeiten und mehr</p>
    <div class="cta">www.hausdienst-velmar.example</div>
    <div class="house-photo" role="img" aria-label="Foto eines modernen Wohnhauses mit Holzfassade und Glasbalkon"></div>
  </section>
</body>
</html>
```